label design for soy candle

I am a start up making soy candles and other products involving scents.
On the label should be in writing : Wild Amber, Handgemacht in der Schweiz, Sojakerze, my logo with the name Thorvel Candles on it. I will upload the currant label of my candles, but I want something more fashioned. The color of the label should be black with Wild Amber written in gold, and the rest in white. Or maybe suggest something different, I am open to new designs. I am also open to change the logo, except the flower has to stay.
Sizes : square 60x60mm / round 50mm / rectangle 70x20mm ( for different jars )

```html
<!DOCTYPE html>
<html lang="de">
<head>
<meta charset="utf-8">
<title>Thorvel Candles – Etiketten Sojakerze</title>
<link rel="stylesheet" href="https://fonts.googleapis.com/css2?family=Poppins:wght@300;400;500&family=Sacramento&display=swap">
<style>
  :root {
    --page: #ffffff;
    --label: #000000;
    --text: #ffffff;
    --gold-dark: #8c6a3b;
    --gold-mid: #c0904f;
    --gold-light: #f4c27b;
    --gold-line: linear-gradient(90deg, var(--gold-dark) 0%, var(--gold-mid) 30%, var(--gold-light) 55%, var(--gold-mid) 75%, var(--gold-dark) 100%);
    --gold-script: linear-gradient(90deg, #8f6d3d 0%, #b48848 40%, #e2b06a 70%, #f4c27b 100%);
  }
  * { margin: 0; padding: 0; box-sizing: border-box; }
  html, body { width: 1200px; height: 799px; overflow: hidden; background: var(--page); }
  body { position: relative; font-family: "Poppins", sans-serif; color: var(--text); }

  .label { position: absolute; background: var(--label); overflow: hidden; }
  .label--round { left: 120px; top: 140px; width: 399px; height: 399px; border-radius: 50%; }
  .label--square { left: 598px; top: 61px; width: 479px; height: 478px; }
  .label--strip { left: 518px; top: 577px; width: 558px; height: 160px; }

  .line { position: absolute; left: 0; right: 0; white-space: nowrap; }
  .centered { text-align: center; }

  .brand-mark { position: absolute; border-radius: 50%; background: var(--text); }
  .brand-name { font-weight: 400; letter-spacing: 0.1em; line-height: 1; }
  .scent-name {
    font-family: "Sacramento", cursive;
    line-height: 1;
    background: var(--gold-script);
    -webkit-background-clip: text; background-clip: text;
    color: transparent;
  }
  .product-type { font-weight: 500; letter-spacing: 0.1em; line-height: 1; }
  .origin { font-weight: 300; letter-spacing: 0.08em; line-height: 1; }

  .gold-rule { position: absolute; left: 0; right: 0; background: var(--gold-line); }
  .pattern-band {
    position: absolute; left: 0; right: 0; bottom: 0;
    background:
      radial-gradient(ellipse at 50% 0%, rgba(214,164,96,0.55), rgba(0,0,0,0) 60%),
      linear-gradient(90deg, #2a1e10 0%, #5a4226 25%, #3a2a16 50%, #6b4e2c 75%, #2a1e10 100%);
  }

  /* round 50mm */
  .label--round .brand-mark { left: 185px; top: 56px; width: 28px; height: 28px; }
  .label--round .brand-name { top: 111px; font-size: 19.5px; }
  .label--round .scent-name { top: 158px; font-size: 66px; }
  .label--round .product-type { top: 251px; font-size: 18px; }
  .label--round .origin { top: 291px; font-size: 13.5px; }
  .label--round .gold-rule { top: 330px; height: 5px; }
  .label--round .pattern-band { top: 335px; }

  /* square 60x60mm */
  .label--square .brand-mark { left: 224px; top: 70px; width: 30px; height: 30px; }
  .label--square .brand-name { top: 133px; font-size: 24px; }
  .label--square .scent-name { top: 190px; font-size: 84px; }
  .label--square .product-type { top: 301px; font-size: 23px; }
  .label--square .origin { top: 350px; font-size: 17.5px; }
  .label--square .gold-rule { top: 396px; height: 5px; }
  .label--square .pattern-band { top: 401px; }

  /* rectangle 70x20mm */
  .label--strip .scent-name { left: 66px; right: auto; top: 20px; font-size: 54px; }
  .label--strip .product-type { left: 66px; right: auto; top: 67px; font-size: 13px; letter-spacing: 0.08em; }
  .label--strip .origin { left: 66px; right: auto; top: 88px; font-size: 10px; letter-spacing: 0.04em; }
  .label--strip .brand-mark { left: 391px; top: 36px; width: 22px; height: 22px; }
  .label--strip .brand-name { left: 292px; right: auto; width: 220px; top: 81px; font-size: 17.5px; text-align: center; }
  .label--strip .gold-rule { top: 113px; height: 5px; }
  .label--strip .pattern-band { top: 118px; }
</style>
</head>
<body>

  <section class="label label--round" aria-label="Rundes Etikett 50 mm">
    <span class="brand-mark" aria-hidden="true"></span>
    <p class="line centered brand-name">THORVEL CANDLES</p>
    <p class="line centered scent-name">Wild Amber</p>
    <p class="line centered product-type">SOJAKERZE</p>
    <p class="line centered origin">HANDGEMACHT IN DER SCHWEIZ</p>
    <div class="gold-rule"></div>
    <div class="pattern-band" role="img" aria-label="Goldenes florales Linienmuster auf Schwarz"></div>
  </section>

  <section class="label label--square" aria-label="Quadratisches Etikett 60 x 60 mm">
    <span class="brand-mark" aria-hidden="true"></span>
    <p class="line centered brand-name">THORVEL CANDLES</p>
    <p class="line centered scent-name">Wild Amber</p>
    <p class="line centered product-type">SOJAKERZE</p>
    <p class="line centered origin">HANDGEMACHT IN DER SCHWEIZ</p>
    <div class="gold-rule"></div>
    <div class="pattern-band" role="img" aria-label="Goldenes florales Linienmuster auf Schwarz"></div>
  </section>

  <section class="label label--strip" aria-label="Rechteckiges Etikett 70 x 20 mm">
    <p class="line scent-name">Wild Amber</p>
    <p class="line product-type">SOJAKERZE</p>
    <p class="line origin">HANDGEMACHT IN DER SCHWEIZ</p>
    <span class="brand-mark" aria-hidden="true"></span>
    <p class="line brand-name">THORVEL CANDLES</p>
    <div class="gold-rule"></div>
    <div class="pattern-band" role="img" aria-label="Goldenes florales Linienmuster auf Schwarz"></div>
  </section>

</body>
</html>
```